Medical program Ombo produce by VALORENZA

I need a business card of the program to give to the customer to get the general information to contact the clinic. I need a bilingual card French and English you will see the logo.
That's a program that the Clinic Valorenza offers. https://medicalombo.ca
Program: Ombo Medical Program
Slogan: Lose weight - Exist - Live / GET FIT - MOVE - LIVE
The clinic that offers the program: Valorenza
Website: https://medicalombo.ca
---
Medical team / Medical team
email: doc@valorenza.ca
phone: 514 555-0147
Information
email: ombo@valorenza.ca
phone: 514 555-0183 ext 3
Target Market(s)
Every person that needs to lose weight
Industry/Entity Type
Health clinic for obese person
Contact Information for Business Card
All the information in the description
Requirements
Must have
- Look clean - Expensive clinic / Need to be bilingual
Nice to have
- Recto verso for french and english
Should not have
- -

```html
<!DOCTYPE html>
<html lang="en">
<head>
<meta charset="utf-8">
<title>Ombo Medical Program – Business Cards</title>
<link rel="stylesheet" href="https://fonts.googleapis.com/css2?family=Quicksand:wght@400;500;600;700&family=Montserrat:wght@600;700&display=swap">
<style>
  :root {
    --bg: #ababab;
    --card: #ffffff;
    --band-grey: #9c9c9c;
    --band-blue: #3592d4;
    --band-teal: #00a99d;
    --brand-teal: #1aa9b8;
    --ink: #222222;
    --text-grey: #777777;
    --divider: #c9c9c9;
    --accent-red: #c8202f;
  }
  * { box-sizing: border-box; margin: 0; padding: 0; }
  html, body { width: 1200px; height: 1000px; overflow: hidden; }
  body { background: var(--bg); position: relative; font-family: "Quicksand", sans-serif; }

  .card {
    position: absolute; top: 338px; width: 514px; height: 296px;
    background: var(--card);
  }
  .card--fr { left: 66px; }
  .card--en { left: 626px; }

  .card__brand { position: absolute; top: 0; left: 0; width: 100%; height: 106px; }
  .program-name {
    position: absolute; left: 132px; top: 34px;
    font-family: "Quicksand", sans-serif; font-weight: 700; font-size: 40px;
    color: var(--brand-teal); letter-spacing: 1px; line-height: 1;
  }
  .brand-divider {
    position: absolute; left: 259px; top: 16px; width: 1px; height: 68px;
    background: var(--divider);
  }
  .powered-by {
    position: absolute; left: 268px; top: 23px;
    font-family: "Montserrat", sans-serif; font-weight: 600; font-size: 8px; color: var(--text-grey);
  }
  .clinic-name {
    position: absolute; left: 268px; top: 45px; display: flex; align-items: center; gap: 5px;
    font-family: "Montserrat", sans-serif; font-weight: 700; font-size: 13px; color: var(--ink);
  }
  .clinic-name__mark { width: 12px; height: 12px; background: var(--accent-red); }

  .band { position: absolute; left: 0; width: 100%; color: #fff; text-align: center; }
  .band--program {
    top: 106px; height: 24px; background: var(--band-grey);
    font-family: "Montserrat", sans-serif; font-weight: 700; font-size: 14px;
    letter-spacing: 2.6px; line-height: 26px;
  }
  .band--slogan {
    top: 130px; height: 54px; background: var(--band-blue);
    font-family: "Montserrat", sans-serif; font-weight: 600; font-size: 36px; line-height: 56px;
  }
  .band--web {
    top: 184px; height: 35px; background: var(--band-teal);
    font-weight: 700; font-size: 22px; line-height: 35px;
  }

  .contacts {
    position: absolute; top: 233px; left: 0; width: 100%;
    display: flex; justify-content: center; gap: 28px; text-align: center;
  }
  .contact__title { font-weight: 700; font-size: 15px; color: var(--band-teal); line-height: 18px; }
  .contact__line { font-weight: 500; font-size: 13.5px; color: var(--text-grey); line-height: 16px; }
</style>
</head>
<body>

  <section class="card card--fr" lang="fr">
    <header class="card__brand">
      <div class="program-name">Ombo</div>
      <div class="brand-divider"></div>
      <div class="powered-by">Powered by</div>
      <div class="clinic-name"><span class="clinic-name__mark"></span>VALORENZA</div>
    </header>
    <div class="band band--program">OMBO MEDICAL PROGRAM</div>
    <div class="band band--slogan">MINCIR - BOUGER - VIVRE</div>
    <div class="band band--web">www.medicalombo.ca</div>
    <div class="contacts">
      <div class="contact">
        <div class="contact__title">Medical team</div>
        <div class="contact__line">doc@valorenza.ca</div>
        <div class="contact__line">514 555-0147</div>
      </div>
      <div class="contact">
        <div class="contact__title">Information</div>
        <div class="contact__line">ombo@valorenza.ca</div>
        <div class="contact__line">514 555-0183 ext 3</div>
      </div>
    </div>
  </section>

  <section class="card card--en" lang="en">
    <header class="card__brand">
      <div class="program-name">Ombo</div>
      <div class="brand-divider"></div>
      <div class="powered-by">Powered by</div>
      <div class="clinic-name"><span class="clinic-name__mark"></span>VALORENZA</div>
    </header>
    <div class="band band--program">OMBO MEDICAL PROGRAM</div>
    <div class="band band--slogan">GET FIT - MOVE - LIVE</div>
    <div class="band band--web">www.medicalombo.ca</div>
    <div class="contacts">
      <div class="contact">
        <div class="contact__title">Medical team</div>
        <div class="contact__line">doc@valorenza.ca</div>
        <div class="contact__line">514 555-0147</div>
      </div>
      <div class="contact">
        <div class="contact__title">Information</div>
        <div class="contact__line">ombo@valorenza.ca</div>
        <div class="contact__line">514 555-0183 ext 3</div>
      </div>
    </div>
  </section>

</body>
</html>
```